Step and Repeat Backdrop for wedding reception photo booth

Would like to have a Step and Repeat Backdrop (8 foot high by 10 foot wide) that incorporates the wedding logo (attached) and the names Elena and Gavin. Background should be white, and wedding colors are burgundy and gold. Show me creativity :-) I have included some random samples.

```html
<!DOCTYPE html>
<html lang="en">
<head>
<meta charset="utf-8">
<title>Elena and Gavin – Step and Repeat Backdrop</title>
<link rel="stylesheet" href="https://fonts.googleapis.com/css2?family=Libre+Baskerville:wght@400&display=swap">
<style>
  :root {
    --page: #ffffff;
    --backdrop: #ffffff;
    --burgundy: #8a1538;
    --gold: #b8965a;
    --edge: rgba(0, 0, 0, 0.2);
  }
  html, body {
    margin: 0;
    padding: 0;
    width: 1200px;
    height: 1200px;
    overflow: hidden;
    background: var(--page);
  }
  .canvas {
    position: relative;
    width: 1200px;
    height: 1200px;
  }
  .backdrop {
    position: absolute;
    left: 40px;
    top: 152px;
    width: 1120px;
    height: 896px;
    box-sizing: border-box;
    padding: 0 28px;
    background: var(--backdrop);
    box-shadow: 0 4px 14px var(--edge);
    display: grid;
    grid-template-columns: repeat(5, minmax(0, 1fr));
    grid-template-rows: repeat(4, minmax(0, 1fr));
    overflow: hidden;
  }
  .tile {
    min-width: 0;
    display: flex;
    align-items: center;
    justify-content: center;
    text-align: center;
    font-family: "Libre Baskerville", serif;
    font-weight: 400;
  }
  .names {
    flex-direction: column;
    color: var(--burgundy);
    font-size: 36px;
    line-height: 44px;
    letter-spacing: 0.14em;
  }
  .names span {
    display: block;
    white-space: nowrap;
    margin-right: -0.14em;
  }
  .monogram {
    color: var(--gold);
    font-size: 72px;
    letter-spacing: -0.02em;
    white-space: nowrap;
  }
</style>
</head>
<body>
<div class="canvas">
  <section class="backdrop" aria-label="Step and repeat backdrop">
    <div class="tile monogram">E&amp;G</div>
    <div class="tile names"><span>Elena</span><span>and</span><span>Gavin</span></div>
    <div class="tile monogram">E&amp;G</div>
    <div class="tile names"><span>Elena</span><span>and</span><span>Gavin</span></div>
    <div class="tile monogram">E&amp;G</div>

    <div class="tile names"><span>Elena</span><span>and</span><span>Gavin</span></div>
    <div class="tile monogram">E&amp;G</div>
    <div class="tile names"><span>Elena</span><span>and</span><span>Gavin</span></div>
    <div class="tile monogram">E&amp;G</div>
    <div class="tile names"><span>Elena</span><span>and</span><span>Gavin</span></div>

    <div class="tile monogram">E&amp;G</div>
    <div class="tile names"><span>Elena</span><span>and</span><span>Gavin</span></div>
    <div class="tile monogram">E&amp;G</div>
    <div class="tile names"><span>Elena</span><span>and</span><span>Gavin</span></div>
    <div class="tile monogram">E&amp;G</div>

    <div class="tile names"><span>Elena</span><span>and</span><span>Gavin</span></div>
    <div class="tile monogram">E&amp;G</div>
    <div class="tile names"><span>Elena</span><span>and</span><span>Gavin</span></div>
    <div class="tile monogram">E&amp;G</div>
    <div class="tile names"><span>Elena</span><span>and</span><span>Gavin</span></div>
  </section>
</div>
</body>
</html>
```